Flyer "Pinch Analysis"-Energy Optimization procedure for Industry

We need a flyer (1xA4 recto/verso )design for a new part of our business.

In Summary: we want to communicate that we are providing "Pinch Analysis" for the industry. It's an energy optimization procedure. We are a cutting edge engineering consulting group.

All details about project in the attached files

Target Market(s)

Engineering

Industry/Entity Type

Business

Font styles to use
Serif

Requirements
Must have
• Finale document in .ai format ready for printing
• More informations in attached files
Nice to have
• See attached files

```html
<!DOCTYPE html>
<html lang="fr">
<head>
<meta charset="utf-8">
<title>Analyse Pinch – Flyer</title>
<link href="https://fonts.googleapis.com/css2?family=Exo+2:wght@400;600;700&family=Roboto:wght@400&display=swap" rel="stylesheet">
<style>
  :root{
    --brand:#3bb5e8;
    --navy:#1e2a8c;
    --red:#e11b22;
    --ink:#3a3a3a;
    --paper:#ffffff;
    --stage:#e7e4df;
  }
  *{box-sizing:border-box;margin:0;padding:0}
  html,body{width:1200px;height:1000px;overflow:hidden;background:var(--stage)}
  .canvas{position:relative;width:1200px;height:1000px}
  .page{position:absolute;left:260px;width:675px;height:477px;background:var(--paper);overflow:hidden;box-shadow:0 2px 8px rgba(0,0,0,.25)}
  .page--front{top:15px;background:linear-gradient(135deg,#f4f5f6,#e4e7ea)}
  .page--back{top:505px;height:478px}
  .art{position:absolute;inset:0}
  .brand{position:absolute;display:flex;align-items:center;gap:7px;font-family:'Exo 2',sans-serif;font-weight:700;color:var(--brand);white-space:nowrap}
  .brand__dot{width:12px;height:12px;border-radius:50%;background:var(--brand);flex:none}
  .brand--front{left:22px;top:34px;font-size:19px}
  .brand--back{left:12px;top:437px;font-size:14px}
  .brand--back .brand__dot{width:10px;height:10px}
  .front-title{position:absolute;left:22px;top:92px;width:180px;font-family:'Exo 2',sans-serif;font-weight:600;font-size:20px;line-height:30px;color:var(--brand);white-space:nowrap}
  .chart{position:absolute;left:0;top:290px}
  .title-band{position:absolute;left:0;top:25px;width:455px;height:42px;background:var(--brand);color:#fff;font-family:'Exo 2',sans-serif;font-weight:600;font-size:14px;line-height:17px;padding:4px 0 0 25px;white-space:nowrap}
  .body{position:absolute;left:25px;top:80px;width:378px;font-family:'Roboto',sans-serif;font-size:7.3px;line-height:10.2px;color:var(--ink)}
  .body p{text-indent:8px;margin-bottom:10.5px}
  .body ul{list-style:none}
  .body li::before{content:"•"}
  .contact-band{position:absolute;left:0;top:402px;width:455px;height:19px;background:var(--brand);color:#fff;font-family:'Exo 2',sans-serif;font-size:13px;line-height:19px;padding-left:12px}
  .address{position:absolute;left:197px;top:432px;font-family:'Roboto',sans-serif;font-style:normal;font-size:7.4px;line-height:10.5px;color:var(--ink)}
</style>
</head>
<body>
<div class="canvas">

  <section class="page page--front">
    <svg class="art" width="675" height="477" viewBox="0 0 675 477">
      <defs>
        <linearGradient id="steel" x1="0" y1="0" x2="1" y2="1">
          <stop offset="0" stop-color="#8c9095"/><stop offset=".5" stop-color="#c9cdd1"/><stop offset="1" stop-color="#4f5358"/>
        </linearGradient>
      </defs>
      <path role="img" aria-label="Photo d'une installation industrielle avec tuyauteries et structures métalliques" d="M330 0 Q170 238 333 477 L675 477 L675 0 Z" fill="url(#steel)"/>
      <path d="M312 0 Q150 238 318 477" fill="none" stroke="var(--brand)" stroke-width="6"/>
    </svg>
    <div class="brand brand--front"><span class="brand__dot"></span>Helvion Engineering</div>
    <h1 class="front-title">Analyse Pinch –<br>en route vers la<br>performance<br>opérationnelle<br>et l’efficacité<br>énergétique</h1>
    <svg class="chart" width="300" height="187" viewBox="0 0 300 187" font-family="Roboto, sans-serif" font-size="5" fill="#333">
      <line x1="22" y1="10" x2="22" y2="170" stroke="#555" stroke-width=".6"/>
      <line x1="22" y1="170" x2="290" y2="170" stroke="#555" stroke-width=".6"/>
      <g text-anchor="end">
        <text x="19" y="12">140</text><text x="19" y="38">120</text><text x="19" y="65">100</text>
        <text x="19" y="92">80</text><text x="19" y="118">60</text><text x="19" y="145">40</text><text x="19" y="171">20</text>
      </g>
      <g text-anchor="middle">
        <text x="22" y="178">0</text><text x="60" y="178">100</text><text x="98" y="178">200</text><text x="136" y="178">300</text>
        <text x="174" y="178">400</text><text x="212" y="178">500</text><text x="250" y="178">600</text><text x="288" y="178">700</text>
      </g>
      <text x="248" y="165" font-weight="700">Heat Flow (kW)</text>
      <text transform="translate(30 70) rotate(-90)" font-weight="700">Actual Temperature °C</text>
      <polyline points="22,167 71,156 121,120 121,93" fill="none" stroke="var(--red)" stroke-width="2"/>
      <polyline points="49,173 170,110 185,40 227,40" fill="none" stroke="var(--navy)" stroke-width="2"/>
    </svg>
  </section>

  <section class="page page--back">
    <svg class="art" width="675" height="478" viewBox="0 0 675 478">
      <path role="img" aria-label="Photo d'une salle technique avec réservoirs et tuyauteries" d="M675 0 L540 0 Q445 100 455 230 L675 230 Z" fill="#9ea3a8"/>
      <path d="M535 0 Q438 100 450 225" fill="none" stroke="var(--brand)" stroke-width="5"/>
      <circle role="img" aria-label="Photo d'une installation de traitement avec cuves bleues et conduites" cx="575" cy="360" r="152" fill="#2f5f9e"/>
      <circle cx="575" cy="360" r="154" fill="none" stroke="var(--brand)" stroke-width="5"/>
    </svg>
    <h2 class="title-band">Analyse Pinch – en route vers la performance<br>opérationnelle et l’efficacité énergétique</h2>
    <div class="body">
      <p>La performance opérationnelle et l’efficacité énergétique sont les clés de la réussite de l’industrie de demain.</p>
      <p>Fort d’une longue expérience dans l’analyse, la conception et la mise en service d’installations industrielles (chimie, alimentaire, pharmacie…), la société Helvion utilise l’analyse Pinch dans sa démarche de conception et d’amélioration.</p>
      <p style="margin-bottom:0">L’analyse Pinch est une méthode d’analyse systématique développée et appliquée depuis les années 1980, elle permet de répondre aux questions suivantes:</p>
      <ul style="margin-bottom:10.5px">
        <li>Quels sont les besoins de chaleur et de froid minimaux de mon procédé</li>
        <li>Quel est mon potentiel de réduction de consommation énergétique</li>
        <li>Quel est la solution technique présentant les coûts minimaux entre investissements et économies</li>
      </ul>
      <p>L’amélioration de l’efficacité énergétique est liée directement à l’exploitation des potentiels de récupération du procédé. Des potentiels de diminution de la consommation de 10 à 30% sont usuels. Nous pouvons également améliorer les performances opérationnelles en analysant vos méthodes de fabrication.</p>
      <p>L’analyse Pinch est aussi bien adaptée pour les PME que pour les grandes entreprises dont les procédés sont exploités de manière continue ou discontinue (batch).</p>
      <p>Etant donné les objectifs énergétiques de la confédération, l’agence nationale de l’énergie (ANE) soutient les analyses Pinch à hauteur de 35% pour les procédés continus et de 60% pour les procédés discontinus (batch).</p>
      <p>Pour tous compléments d’informations et pour savoir si une analyse Pinch est justifiée dans votre cas, nous vous conseillons avec plaisir.</p>
    </div>
    <div class="contact-band">Contact:</div>
    <div class="brand brand--back"><span class="brand__dot"></span>Helvion Engineering</div>
    <address class="address">Julien Marmier, Luc Dessimoz<br>Helvion SA<br>Rue des Ateliers 14<br>CH-1950 Sion</address>
  </section>

</div>
</body>
</html>
```